Camp Maplebrook Summer Programs Postcard

We need a postcard design for summer 2017 programs. Camp Maplebrook offers nine weeks of day camp and one week of overnight camp. We are a Christian summer camp. We offer lots of activities like swimming, archery, rock wall, zipline, sports, crafts, drama and more. We want to showcase the activities we offer. The design should communicate outdoor fun and friendship. We want to focus on high quality photos that reflect the activities we offer.

Target Market(s)

Elementary age children/parents

Industry/Entity Type

Childcare

Font styles to use
Serif

Requirements
Must have
• Camp Maplebrook "Christian Camping Since 1952"
• Day Camp 2017 "Courageous Campers"
• June 19 - August 18
• $130 per week
• Mon-Fri 8 am to 4 pm. Open to all kids entering grades 1 to 8. Day camp is chock full of activities like swimming, rock wall, archery, zipline, sports, campfires and much more! Daily lunch and snack included. Before and after-care available at an extra rate.
• Overnight Camp 2017
• July 16 - 22
• $325
• Open to all kids ages 8 to 14. Spend the week making new friends, sleeping in cabins, climbing the rock wall and ziplining under the stars! Our special guest speaker will lead twice daily chapel sessions that will challenge campers to grow in their faith.
• Register and pay for 7 weeks by May 1st, get 2 FREE!
• Website: www.maplebrook-example.org
• Address: 42 Cedar Vale Rd. Dunmore, NH 03990
• Phone: 603-555-0148

```html
<!DOCTYPE html>
<html lang="en">
<head>
<meta charset="utf-8">
<title>Camp Maplebrook Summer Programs Postcard</title>
<link href="https://fonts.googleapis.com/css2?family=Tinos:wght@400;700&display=swap" rel="stylesheet">
<style>
  :root {
    --backdrop: #8e8c8d;
    --card: #ffffff;
    --camp-red: #a51c24;
    --band-red: #c21f2e;
    --bark: #6b3f1f;
    --ink-light: #ffffff;
    --photo-green: #6f8a4a;
    --photo-leaf: #4f7a3a;
    --photo-sky: #b9c7c9;
    --photo-water: #3d5664;
    --photo-wood: #9a8c74;
  }
  html, body {
    margin: 0;
    padding: 0;
    width: 1189px;
    height: 1200px;
    overflow: hidden;
    background: var(--backdrop);
    font-family: "Tinos", "Times New Roman", serif;
  }
  .postcard {
    position: absolute;
    left: 226px;
    width: 734px;
    height: 489px;
    background: var(--card);
    box-shadow: 3px 3px 4px rgba(0,0,0,0.45);
    overflow: hidden;
  }
  .postcard--front { top: 78px; }
  .postcard--back { top: 637px; }

  /* photo grid */
  .photo {
    position: absolute;
  }
  .photo--team-run {
    left: 7px; top: 7px; width: 342px; height: 300px;
    background: linear-gradient(180deg, var(--photo-wood) 0%, var(--photo-leaf) 40%, var(--photo-green) 100%);
  }
  .photo--smiling-camper {
    left: 355px; top: 7px; width: 166px; height: 148px;
    background: linear-gradient(160deg, var(--photo-leaf) 0%, #c9b9a2 55%, #8a8f86 100%);
  }
  .photo--lake-tubing {
    left: 355px; top: 161px; width: 166px; height: 146px;
    background: linear-gradient(180deg, var(--photo-water) 0%, #c8533e 60%, #d7c23a 100%);
  }
  .photo--rock-wall {
    left: 527px; top: 7px; width: 200px; height: 300px;
    background: linear-gradient(90deg, var(--photo-leaf) 0%, #8a8a86 45%, var(--photo-wood) 100%);
  }

  /* brand lockup */
  .brand {
    position: absolute;
    display: flex;
    align-items: center;
    gap: 9px;
  }
  .brand__dot {
    width: 22px; height: 22px;
    border-radius: 50%;
    background: var(--camp-red);
    flex: none;
  }
  .brand__name {
    font-weight: 700;
    color: var(--camp-red);
    white-space: nowrap;
    line-height: 1;
  }
  .postcard--front .brand { left: 18px; top: 337px; }
  .postcard--front .brand__name { font-size: 31px; }
  .postcard--back .brand { left: 54px; top: 60px; }
  .postcard--back .brand__dot { width: 28px; height: 28px; }
  .postcard--back .brand__name { font-size: 38px; }

  .tagline {
    position: absolute;
    left: 18px; top: 412px;
    margin: 0;
    font-size: 10.5px;
    letter-spacing: 2.6px;
    color: var(--camp-red);
    text-transform: uppercase;
  }

  /* day camp details */
  .day-camp {
    position: absolute;
    left: 300px; top: 322px; width: 420px;
    text-align: center;
    color: var(--camp-red);
    font-weight: 700;
  }
  .day-camp__title { margin: 0; font-size: 18.5px; line-height: 1.2; }
  .day-camp__dates { margin: 9px 0 0; font-size: 17px; }
  .day-camp__price { margin: 6px 0 0; font-size: 17px; }
  .day-camp__amount { font-size: 30px; }

  .info-band {
    position: absolute;
    left: 0; bottom: 0; width: 100%; height: 51px;
    background: var(--band-red);
    color: var(--ink-light);
    box-sizing: border-box;
    padding: 9px 18px 0 19px;
    font-size: 12.4px;
    line-height: 1.3;
  }
  .info-band p { margin: 0; }

  /* overnight panel */
  .overnight {
    position: absolute;
    left: 0; top: 138px; width: 367px; height: 351px;
    background: var(--camp-red);
    color: var(--ink-light);
    box-sizing: border-box;
    padding: 0 20px 0 19px;
  }
  .overnight__title { margin: 37px 0 0; font-size: 16px; font-weight: 400; }
  .overnight__dates { margin: 1px 0 0; font-size: 12.5px; }
  .overnight__body {
    margin: 48px 0 0;
    font-size: 12.4px;
    line-height: 1.32;
    text-align: justify;
  }
  .overnight__offer { margin: 16px 0 0; font-size: 12.4px; }
  .contact { margin: 16px 0 0; font-size: 12.4px; line-height: 1.32; }
  .price-seal {
    position: absolute;
    left: 260px; top: 20px;
    width: 74px; height: 74px;
    border-radius: 50%;
    background: var(--bark);
    box-shadow: 0 0 10px rgba(255,230,200,0.55);
    display: flex;
    align-items: center;
    justify-content: center;
    font-size: 22px;
    transform: rotate(-14deg);
  }
</style>
</head>
<body>

<section class="postcard postcard--front">
  <div class="photo photo--team-run" role="img" aria-label="Photo of campers in pinnies running across a grassy field with a frisbee"></div>
  <div class="photo photo--smiling-camper" role="img" aria-label="Photo of a smiling young camper outdoors"></div>
  <div class="photo photo--lake-tubing" role="img" aria-label="Photo of campers in life jackets on a float in the lake"></div>
  <div class="photo photo--rock-wall" role="img" aria-label="Photo of a camper in a helmet and harness climbing the rock wall"></div>

  <div class="brand">
    <span class="brand__dot"></span>
    <span class="brand__name">Camp Maplebrook</span>
  </div>
  <p class="tagline">Christian Camping Since 1952</p>

  <div class="day-camp">
    <h2 class="day-camp__title">DAY CAMP 2017 "COURAGEOUS CAMPERS"</h2>
    <p class="day-camp__dates">JUNE 19 - AUGUST 18</p>
    <p class="day-camp__price"><span class="day-camp__amount">$130</span> PER WEEK</p>
  </div>

  <div class="info-band">
    <p>Mon-Fri 8 am to 4 pm. Open to all kids entering grades 1 to 8. Day camp is chock full of activities like swimming, rock wall, archery zipline, sports, campfires and much more! Daily lunch and snack included. Before and after-care available at an extra rate.</p>
  </div>
</section>

<section class="postcard postcard--back">
  <div class="brand">
    <span class="brand__dot"></span>
    <span class="brand__name">Camp Maplebrook</span>
  </div>

  <div class="overnight">
    <div class="price-seal">$325</div>
    <h2 class="overnight__title">Overnight Camp 2017</h2>
    <p class="overnight__dates">July 16 - 22</p>
    <p class="overnight__body">Open to all kids ages 8 to 14. Spend the week making new friends, sleeping in cabins, climbing the rock wall and ziplining under the stars! Our special guest speaker will lead twice daily chapel sessions that will challenge campers to grow in their faith.</p>
    <p class="overnight__offer">Register and pay for 7 weeks by May 1st, get 2 FREE!</p>
    <p class="contact">
      Website: www.maplebrook-example.org<br>
      Address: 42 Cedar Vale Rd. Dunmore, NH 03990<br>
      Phone: 603-555-0148
    </p>
  </div>
</section>

</body>
</html>
```